We need a web design for a retail food business based in Greater Western Sydney Australia called Golden Lantern Noodle Restaurant. Basically just need a simple yet easily to navigate website to browse through a menu, gallery , brief description about us, opening hours.
Menu and Gallery will be constantly updated.
Will provide own images for gallery
Updates
Menu has been uploaded and some idea on the colours I would like on the site
Some additional pictures added to see what designs you guys can come up with . Thanks again
To All Designers,
Any extra fee on top of the designs that feels need to be charged, please let me know in advance
Reason: Extending Deadline as I have yet to find a design that I would like...Thanks guys
Target Market(s)
All groups
Industry/Entity Type
Business
Requirements
Must have
- Open minded to any designs
Nice to have
- Would like slideshow behind main logo.
Preferred light coloured site yet not too playful
Should not have
- Preferably no dark colours backgrounds

```html
<!DOCTYPE html>
<html lang="en">
<head>
<meta charset="utf-8">
<title>Golden Lantern Noodle Restaurant</title>
<link href="https://fonts.googleapis.com/css2?family=Amarante&family=Carlito&family=Arimo&display=swap" rel="stylesheet">
<style>
  :root {
    --ink-deep: #3a1222;
    --ink-body: #4a0c12;
    --accent-red: #8e1010;
    --panel-pink: rgba(238, 196, 214, 0.72);
    --sidebar-pink: rgba(242, 190, 212, 0.55);
    --logo-bg: #f4d4dc;
    --logo-red: #b8141e;
    --social-pink: #f9d3de;
    --photo-warm-1: #d9b25e;
    --photo-warm-2: #c86e48;
  }
  * { box-sizing: border-box; margin: 0; padding: 0; }
  html, body { width: 1200px; height: 673px; overflow: hidden; }
  body { position: relative; font-family: "Arimo", Arial, sans-serif; }
  a { text-decoration: none; color: inherit; }

  .hero-backdrop {
    position: absolute; inset: 0;
    background:
      linear-gradient(180deg, rgba(0,0,0,0) 55%, rgba(60,50,48,0.75) 100%),
      linear-gradient(90deg, var(--photo-warm-1) 0%, #c9984e 30%, var(--photo-warm-2) 55%, #b5683f 75%, var(--photo-warm-1) 100%);
  }

  .social-links { position: absolute; top: 4px; left: 987px; display: flex; gap: 5px; }
  .social-links a { width: 25px; height: 25px; border-radius: 50%; background: var(--social-pink); display: block; }

  .sidebar { position: absolute; left: 119px; top: 0; width: 265px; height: 620px; }
  .sidebar-shape { position: absolute; inset: 0; }

  .brand {
    position: absolute; left: 0; top: 0; width: 265px; height: 113px;
    background: var(--logo-bg);
    box-shadow: 0 3px 8px rgba(0,0,0,0.45);
    display: flex; flex-direction: column; align-items: center; justify-content: center;
    text-align: center; color: var(--logo-red);
    font-family: "Arimo", Arial, sans-serif; font-weight: 700;
  }
  .brand-name { font-size: 19px; line-height: 22px; }
  .brand-tag { font-size: 12px; margin-top: 6px; }

  .main-nav { position: absolute; left: 37px; top: 155px; list-style: none; }
  .main-nav li { height: 81px; }
  .main-nav a { display: block; color: var(--ink-deep); }
  .nav-title { font-family: "Amarante", cursive; font-size: 23px; line-height: 26px; display: block; }
  .nav-sub { font-family: "Carlito", "Calibri", sans-serif; font-size: 11px; line-height: 13px; display: block; margin-top: 0; }

  .welcome-panel {
    position: absolute; left: 496px; top: 333px; width: 496px; height: 278px;
    background: var(--panel-pink);
  }
  .welcome-title { position: absolute; left: 30px; top: 13px; font-size: 19px; font-weight: 400; color: #1a0a0a; }
  .welcome-title span { color: var(--accent-red); }
  .chef-photo { position: absolute; left: 25px; top: 64px; width: 139px; height: 186px; background: linear-gradient(180deg, #fafafa, #eee6e4); }
  .welcome-copy { position: absolute; left: 196px; top: 67px; width: 276px; font-size: 13px; line-height: 16px; color: var(--ink-body); }
  .welcome-copy p + p { margin-top: 16px; }
</style>
</head>
<body>
  <div class="hero-backdrop" role="img" aria-label="Restaurant dining room with bar counter, tables and chairs"></div>

  <nav class="social-links" aria-label="Social links">
    <a href="#" aria-label="Social page"></a>
    <a href="#" aria-label="Social feed"></a>
    <a href="#" aria-label="News feed"></a>
  </nav>

  <aside class="sidebar">
    <svg class="sidebar-shape" width="265" height="620" viewBox="0 0 265 620" aria-hidden="true">
      <path d="M0 0 H265 V618 Q132.5 522 0 618 Z" fill="var(--sidebar-pink)"/>
    </svg>

    <div class="brand">
      <span class="brand-name">Golden Lantern<br>Noodle Restaurant</span>
      <span class="brand-tag">LICENSED · PH: (02) 4700 1234</span>
    </div>

    <ul class="main-nav">
      <li><a href="#"><span class="nav-title">ABOUT US</span><span class="nav-sub">More about us</span></a></li>
      <li><a href="#"><span class="nav-title">MENU</span><span class="nav-sub">See our Menu</span></a></li>
      <li><a href="#"><span class="nav-title">GALLERY</span><span class="nav-sub">Enjoy our gallery</span></a></li>
      <li><a href="#"><span class="nav-title">OPENING HOURS</span><span class="nav-sub">Visiting time</span></a></li>
      <li><a href="#"><span class="nav-title">CONTACT US</span><span class="nav-sub">Get in touch with us</span></a></li>
    </ul>
  </aside>

  <section class="welcome-panel">
    <h1 class="welcome-title">Hello <span>There !</span></h1>
    <div class="chef-photo" role="img" aria-label="Chef in white hat and jacket"></div>
    <div class="welcome-copy">
      <p>Ut wisi enim ad minim veniam, quis nostrud exerci tation ullamcorper suscipit lobortis nisl ut aliquip ex ea commodo consequat.</p>
      <p>Duis autem vel eum iriure dolor in hendrerit in vulputate velit esse molestie consequat, vel illum dolore eu feugiat nulla facilisis at vero eros et accumsan et iusto odio dignissim.</p>
      <p>Qui blandit praesent luptatum zzril delenit augue duis dolore te feugait nulla facilisi.</p>
    </div>
  </section>
</body>
</html>
```